Funk up our website

Our website is currently in operation and working well, see it at www.brightpathlegal.co.uk

However it needs some redesign work, to help it feel fresh, inviting and friendly.

We need graphic mockups (png hi-res) to pass to the dev team, to do the css work:

homepage - http://www.brightpathlegal.co.uk
topic page - http://www.brightpathlegal.co.uk/guidance/business
sub-topic - http://www.brightpathlegal.co.uk/guidance/business/goods-services
content - http://www.brightpathlegal.co.uk/guidance/business/goods-services/heads-of-terms
ancillary pages - contact us, heads of terms, etc

The structure of the page in terms of the placement of header, menu bar, content area and footer needs to remain, but the design of it is up for grabs.

The site is currently free to use, but in the future will have the aim of getting users to register for free, but with the option of buying documents on an individual basis, or subscription basis, or subscribing to additional legal services.

Additional information
---------------------------
Users
1. Owners and managers in small and medium businesses
2. In the UK only
3. Who find dealing with legal issues and lawyers intimidating
4. Who are searching for online help to try and avoid having to deal with a lawyer
5. Or have been referred via social media
Desired user experience
1. A welcoming, friendly site
2. That takes the complexity out of dealing with legal issues
3. That really does Brightpath Legal
4. That is fast, efficient and clear
5. That is pleasantly different from the normal experience of interacting with a law firm
Relevant factors
1. Most visitors will first land on a content page (e.g. [link]) via a search result or banner advertisement – not the Home Page
2. Repeat visitors are more likely to go to the Home Page
3. Works with web responsive design techniques for display on smartphones and tablets
4. Implemented through CSS
Colour palette
Designer should feel able to build the palette around the following core colours
CMYK
YELLOW = 0,25,100,0
GREEN = 80,0,100,0
BLUE = 100,25,0,0

RGB
YELLOW = 255,195,15
GREEN = 15,175,75
BLUE = 0,140,210

PANTONE
YELLOW = 123c
GREEN = 361c
BLUE = 3005c

Fonts
Soho Gothic, Soho, Arial
Designer should feel able to add fonts to complement these core fonts.

Our logo needs to remain (see attached document) Our strap line, can be changed if needed.

Best
RM
Updates

Hi All

Some websites worth having a look at for how people have done things differently / added something distinctive to their website:

http://www.quorvanlegal.co.uk/
https://www.tidewellcounsel.co.uk/
http://www.brevatrix.com/

Cheers
RM

Hi All

Thanks for your designs. Just back in the office today, we will discuss and feedback / decide asap.

Best
RM

```html
<!DOCTYPE html>
<html lang="en">
<head>
<meta charset="utf-8">
<title>Brightpath Legal – Home</title>
<link href="https://fonts.googleapis.com/css2?family=Roboto:wght@300;400;500;700&family=PT+Sans:wght@400;700&family=PT+Sans+Narrow:wght@400;700&display=swap" rel="stylesheet">
<style>
  :root{
    --yellow:#ffc30f;
    --green:#0faf4b;
    --green-dark:#0d8f3e;
    --blue:#008cd2;
    --ink:#222;
    --text:#444;
    --muted:#666;
    --link:#1a4f8a;
    --red:#e0161c;
    --line:#d7d7d7;
    --panel:#f4f4f6;
    --footer:#2b2b2b;
  }
  *{box-sizing:border-box;margin:0;padding:0}
  html,body{width:1040px;height:1200px;overflow:hidden;background:#fff}
  body{position:relative;font-family:"Roboto",Arial,sans-serif;color:var(--text)}
  .abs{position:absolute}

  /* Header */
  .site-header{position:absolute;left:0;top:0;width:1040px;height:114px;border-top:2px solid var(--yellow);background:linear-gradient(#fff,#f7f7f7)}
  .brand{position:absolute;left:99px;top:22px;display:flex;align-items:center;gap:12px}
  .brand-mark{width:72px;height:72px;background:var(--green)}
  .brand-name{font-family:"PT Sans",Arial,sans-serif;font-weight:700;font-size:36px;line-height:38px;color:var(--ink);width:170px}
  .strapline{position:absolute;left:457px;top:38px;font-family:"PT Sans",Arial,sans-serif;font-size:21px;line-height:26px;color:var(--ink)}
  .strapline .accent{display:block;padding-left:56px}
  .strapline .y{color:var(--yellow)} .strapline .g{color:var(--green)} .strapline .b{color:var(--blue)}
  .account{position:absolute;right:108px;top:21px;display:flex;gap:26px;font-size:12px;color:var(--ink)}
  .account span{display:flex;align-items:center;gap:7px}
  .search{position:absolute;left:738px;top:59px;width:194px;height:25px;border:1px solid #c9c9c9;border-radius:4px;background:#fff;overflow:hidden}
  .search .ph{position:absolute;left:38px;top:6px;font-size:11px;color:#999}
  .search svg{position:absolute;left:12px;top:5px}
  .search .go{position:absolute;right:0;top:0;width:36px;height:23px;background:var(--yellow);color:#fff;font-size:11px;text-align:center;line-height:23px}

  /* Nav */
  .main-nav{position:absolute;left:0;top:114px;width:1040px;height:39px;background:linear-gradient(#fcfcfc,#eee);border-top:1px solid #e2e2e2;border-bottom:1px solid #cfcfcf}
  .main-nav a{position:absolute;top:12px;font-size:13px;color:var(--ink);text-decoration:none;transform:translateX(-50%)}
  .main-nav .sep{position:absolute;top:0;width:1px;height:38px;background:#dcdcdc}
  .main-nav .active-bar{position:absolute;left:106px;top:35px;width:85px;height:3px;background:var(--green)}

  /* Hero */
  .hero{position:absolute;left:0;top:153px;width:1040px;height:386px;background:radial-gradient(ellipse at 78% 55%,#fafafa 0%,#ececec 60%,#dedede 100%);border-bottom:2px solid #cfcfcf}
  .player{position:absolute;left:100px;top:32px;width:526px;height:321px;background:#111}
  .player .screen{position:absolute;left:13px;top:13px;width:498px;height:268px;background:linear-gradient(135deg,#fdfdfd,#e9e9e9)}
  .player .bar{position:absolute;left:0;bottom:0;width:526px;height:31px;background:#1b1b1b}
  .player .progress{position:absolute;left:0;top:-3px;width:526px;height:3px;background:#555}
  .player .progress i{position:absolute;left:0;top:0;width:44px;height:3px;background:#d41f1f}
  .player .time{position:absolute;left:75px;top:9px;font-size:10px;color:#ddd}
  .hero-copy{position:absolute;right:107px;top:76px;text-align:right;color:var(--ink);font-weight:300}
  .hero-copy .l1{font-size:21px}
  .hero-copy .l2{font-size:27px;margin-top:4px}
  .hero-copy .l3{font-size:16px;margin-top:14px;line-height:26px}
  .hero-copy .free{color:var(--red)}
  .cta{position:absolute;left:691px;top:227px;width:241px;height:60px;background:var(--green);border:2px solid #fff;box-shadow:0 1px 3px rgba(0,0,0,.3);text-align:center;font-size:18px;line-height:25px;padding-top:5px;color:#fff}
  .cta .y{color:var(--yellow)}
  .dots{position:absolute;left:880px;top:318px;display:flex;gap:11px}
  .dots i{width:6px;height:6px;background:var(--green)}
  .dots i.on{background:var(--blue)}

  /* Guidance */
  .section-title{position:absolute;left:104px;top:568px;font-size:21px;color:var(--ink)}
  .section-title em{font-style:normal;color:var(--green)}
  .guide{position:absolute;top:611px}
  .guide .icon{position:absolute;left:0;top:0;width:74px;height:74px;border-radius:6px}
  .guide h3{position:absolute;top:0;font-weight:400;font-size:18px;color:var(--ink);white-space:nowrap}
  .guide ul{position:absolute;top:28px;list-style:none;font-size:12.5px;line-height:18.2px;color:var(--text);white-space:nowrap}
  .guide li::before{content:"›";margin-right:7px;color:var(--muted)}
  .guide p{position:absolute;top:28px;font-size:12.5px;line-height:18.2px;width:150px}

  /* Testimonials */
  .testimonials{position:absolute;left:100px;top:768px;width:537px;height:276px;border:1px solid #c8c8c8;background:var(--panel)}
  .testimonials .head{height:47px;background:linear-gradient(#f9f9fb,#eceef1);border-bottom:1px solid #e2e2e2;padding:12px 0 0 16px;font-family:"PT Sans Narrow",Arial,sans-serif;font-size:18px;color:var(--ink)}
  .testimonials .arrows{position:absolute;right:20px;top:17px}
  .quote{position:absolute;left:18px;width:500px}
  .avatar{position:absolute;left:0;top:0;width:88px;height:88px;border-radius:50%;border:4px solid #fff;box-shadow:0 0 0 1px #ccc;background:radial-gradient(circle at 50% 40%,#b98a6a,#6b4a33)}
  .quote .mark{position:absolute;left:94px;top:6px;font-family:Georgia,serif;font-size:22px;color:var(--ink)}
  .quote p{position:absolute;left:115px;top:16px;width:382px;font-family:"PT Sans",Arial,sans-serif;font-size:11.2px;line-height:15.5px;color:var(--muted);text-align:justify}
  .quote cite{position:absolute;left:118px;font-style:normal;font-family:"PT Sans",Arial,sans-serif;font-size:11.5px;color:var(--link)}

  /* Lawyers */
  .lawyers{position:absolute;left:670px;top:766px;width:259px;height:279px;border:1px solid #ddd;background:#fff}
  .lawyers .head{height:35px;background:var(--green);color:#fff;font-family:"PT Sans Narrow",Arial,sans-serif;font-size:18px;padding:7px 0 0 16px}
  .lawyer{position:absolute;left:7px;width:248px;height:74px}
  .lawyer .photo{position:absolute;left:0;top:0;width:93px;height:71px;border:2px solid #ddd;background:linear-gradient(135deg,#8a5a32,#3a2a22)}
  .lawyer h4{position:absolute;left:102px;top:-4px;font-family:"PT Sans Narrow",Arial,sans-serif;font-weight:400;font-size:14px;color:var(--ink);white-space:nowrap}
  .lawyer p{position:absolute;left:102px;top:16px;width:144px;font-family:"PT Sans Narrow",Arial,sans-serif;font-size:10px;line-height:13.8px;color:var(--ink)}
  .lawyer .more{display:block;color:var(--red)}

  /* Footer */
  .site-footer{position:absolute;left:0;top:1076px;width:1040px;height:124px;background:repeating-linear-gradient(45deg,#2e2e2e 0 2px,#262626 2px 4px)}
  .site-footer h5{position:absolute;left:121px;top:20px;font-family:"PT Sans Narrow",Arial,sans-serif;font-weight:400;font-size:20px;color:#fff;font-variant:small-caps}
  .email{position:absolute;left:120px;top:56px;width:205px;height:32px;border-radius:6px;background:#fff;font-family:"PT Sans",Arial,sans-serif;font-size:10.5px;color:#555;padding:9px 0 0 13px}
  .subscribe{position:absolute;left:339px;top:57px;width:80px;height:29px;border-radius:5px;background:var(--green);color:#fff;font-family:"PT Sans",Arial,sans-serif;font-size:14px;text-align:center;line-height:29px}
  .social{position:absolute;left:765px;top:19px;display:flex;gap:11px}
  .social i{width:22px;height:22px;display:block}
  .copyright{position:absolute;right:121px;top:58px;font-family:"PT Sans Narrow",Arial,sans-serif;font-size:12px;color:#ddd}
</style>
</head>
<body>

<header class="site-header">
  <div class="brand">
    <div class="brand-mark"></div>
    <div class="brand-name">Brightpath Legal</div>
  </div>
  <div class="strapline">Making legal services<span class="accent"><span class="y">fast,</span> <span class="g">efficient</span> <span class="b">&amp; clear.</span></span></div>
  <div class="account">
    <span><svg width="10" height="13" viewBox="0 0 10 13"><rect x="0" y="5" width="10" height="8" rx="1" fill="#222"/><path d="M2.5 5V3.5a2.5 2.5 0 0 1 5 0V5" stroke="#222" stroke-width="1.6" fill="none"/></svg>Login</span>
    <span><svg width="12" height="13" viewBox="0 0 12 13"><rect x="0" y="1" width="12" height="12" rx="1" fill="#222"/><path d="M3 5h6M3 8h6M3 11h4" stroke="#fff" stroke-width="1"/></svg>Register</span>
  </div>
  <div class="search">
    <svg width="16" height="16" viewBox="0 0 16 16"><circle cx="6" cy="6" r="4.5" stroke="#888" stroke-width="1.6" fill="none"/><path d="M9.5 9.5l4 4" stroke="#888" stroke-width="2"/></svg>
    <span class="ph">Search</span>
    <span class="go">GO</span>
  </div>
</header>

<nav class="main-nav">
  <a href="#" style="left:140px">Home</a>
  <span class="sep" style="left:191px"></span>
  <a href="#" style="left:261px">Guide Yourself</a>
  <span class="sep" style="left:329px"></span>
  <a href="#" style="left:402px">Draft Yourself</a>
  <span class="sep" style="left:474px"></span>
  <a href="#" style="left:560px">Search For a Lawyer</a>
  <span class="sep" style="left:648px"></span>
  <a href="#" style="left:722px">Get Your Drafts</a>
  <span class="active-bar"></span>
</nav>

<section class="hero">
  <div class="player">
    <div class="screen" role="img" aria-label="Explainer video still: a hand drawing over a screenshot of the guidance pages"></div>
    <div class="bar">
      <div class="progress"><i></i></div>
      <svg class="abs" style="left:18px;top:9px" width="12" height="13" viewBox="0 0 12 13"><rect x="1" y="0" width="3.5" height="13" fill="#ccc"/><rect x="7.5" y="0" width="3.5" height="13" fill="#ccc"/></svg>
      <svg class="abs" style="left:48px;top:9px" width="16" height="13" viewBox="0 0 16 13"><path d="M0 4h4l5-4v13l-5-4H0z" fill="#ccc"/><path d="M11 3q3 3.5 0 7" stroke="#ccc" fill="none"/></svg>
      <span class="time">0:02 / 0:33</span>
      <svg class="abs" style="left:488px;top:8px" width="16" height="14" viewBox="0 0 16 14"><path d="M1 1h4M1 13h4M1 1v4M1 13V9M15 1h-4M15 13h-4M15 1v4M15 13V9" stroke="#ccc" stroke-width="1.6" fill="none"/></svg>
      <svg class="abs" style="left:460px;top:9px" width="16" height="12" viewBox="0 0 16 12"><rect x="1" y="1" width="14" height="10" stroke="#ccc" stroke-width="1.5" fill="none"/></svg>
    </div>
  </div>

  <div class="hero-copy">
    <div class="l1">Free Legal Support For</div>
    <div class="l2">You and Your Business</div>
    <div class="l3">Guide Yourself, Draft Yourself<br>Help Yourself, it’s <span class="free">FREE</span></div>
  </div>
  <div class="cta">Clickhere to Register and<br><span class="y">Start Drafting for Free</span></div>
  <div class="dots"><i></i><i></i><i class="on"></i><i></i></div>
</section>

<h2 class="section-title" style="font-weight:400">Our <em>Guidance</em></h2>

<div class="guide" style="left:104px">
  <div class="icon" role="img" aria-label="Office building illustration" style="background:linear-gradient(135deg,#c9d6e2,#6f8496)"></div>
  <h3 style="left:83px">Business</h3>
  <ul style="left:88px">
    <li>Trade &amp; e-commerce</li>
    <li>Insolvency</li>
    <li>Employees &amp; staff</li>
    <li>Health and safety</li>
    <li>Business premises</li>
  </ul>
</div>
<div class="guide" style="left:418px">
  <div class="icon" role="img" aria-label="Illustration of a person in a suit" style="width:50px;background:linear-gradient(#d9d9d9,#3a3f48)"></div>
  <h3 style="left:62px">Personal</h3>
  <ul style="left:64px">
    <li>Wills, probate &amp; trusts</li>
    <li>Dealing with employers</li>
  </ul>
</div>
<div class="guide" style="left:684px">
  <div class="icon" role="img" aria-label="Envelope icon" style="width:44px;height:46px;top:12px;background:linear-gradient(#e9f3fb,#4aa3dc)"></div>
  <h3 style="left:56px">Get Your Draft</h3>
  <p style="left:61px">Log in to draft new docu-ments and to edit drafts you’ve saved</p>
</div>

<section class="testimonials">
  <div class="head">TESTIMONIALS</div>
  <svg class="abs" style="right:20px;top:16px" width="26" height="16" viewBox="0 0 26 16"><path d="M8 0v16L0 8z" fill="#111"/><path d="M18 0v16l8-8z" fill="#111"/></svg>

  <div class="quote" style="top:60px">
    <div class="avatar" role="img" aria-label="Portrait photo of a customer"></div>
    <span class="mark">“</span>
    <p>Sed ut perspiciatis unde omnis iste natus error sit voluptatem accusantium doloremque laudantium, totam rem aperiam, eaque ipsa quae ab illo inventore veritatis et quasi architecto beatae vitae dicta sunt explicabo.</p>
    <cite style="top:77px">-- Owen , Newyork</cite>
  </div>
  <div class="quote" style="top:172px">
    <div class="avatar" role="img" aria-label="Portrait photo of a customer couple"></div>
    <span class="mark">“</span>
    <p>Sed ut perspiciatis unde omnis iste natus error sit voluptatem accusantium doloremque laudantium, totam rem aperiam, eaque ipsa quae ab illo inventore veri-tatis et quasi architecto beatae vitae dicta sunt explicabo.</p>
    <cite style="top:73px">-- Elsa, Newyork</cite>
  </div>
</section>

<aside class="lawyers">
  <div class="head">LAWYERS PROFILE</div>
  <div class="lawyer" style="top:41px">
    <div class="photo" role="img" aria-label="Photo of a lawyer in a library"></div>
    <h4>Uenim Minim Veniam Quis</h4>
    <p>Uenim ad minim veniam, quis nostrud laboris nisi utaliquip ex irurdolor into Uenim ad minim <span class="more">More &gt;&gt;</span></p>
  </div>
  <div class="lawyer" style="top:121px">
    <div class="photo" role="img" aria-label="Photo of a lawyer at a desk" style="background:linear-gradient(135deg,#b0643a,#4a2a1e)"></div>
    <h4>Uenim Minim Veniam Quis</h4>
    <p>Uenim ad minim veniam, quis nostrud laboris nisi utaliquip ex irurdolor into Uenim ad minim <span class="more">More &gt;&gt;</span></p>
  </div>
  <div class="lawyer" style="top:202px">
    <div class="photo" role="img" aria-label="Photo of a barrister in a gown" style="background:linear-gradient(135deg,#9a6a3a,#2a2220)"></div>
    <h4>Uenim Minim Veniam Quis</h4>
    <p>Uenim ad minim veniam, quis nostrud laboris nisi utaliquip ex irurdolor into Uenim ad minim <span class="more">More &gt;&gt;</span></p>
  </div>
</aside>

<footer class="site-footer">
  <h5>Get FREE Newsletter</h5>
  <div class="email">Enter Your Email id</div>
  <div class="subscribe">Subscribe</div>
  <div class="social" aria-label="Social links">
    <i style="background:#3b5a9a"></i><i style="background:#2fa8dc"></i><i style="background:#444"></i><i style="background:#e8a020"></i><i style="background:#c4302b"></i>
  </div>
  <div class="copyright">© 2014 brightpathlegal.co.uk, All Rights Reserved</div>
</footer>

</body>
</html>
```